Flyer-Design für Psychotherapeut
Zielgruppe
Angeboten wird als Dienstleistung Psychotherapie, Coaching und Paarberatung
für Einzelpersonen (Männer/Frauen), Paare und Familien in schwierigen privaten und beruflichen Lebenssituationen.
Aufgabenstellung
Sehr geehrte Damen, sehr geehrte Herren,
gewünscht wird ein Falzflyer Hochformat, DIN-Lang, Wickelfalz, 6 bedruckte Seiten mit dem Endformat 10,0 x 21,0 cm. Ein entsprechendes Datenblatt der Druckerei finden Sie im Anhang.
Der Flyer wird auf einer Gesundheitsmesse eingesetzt und soll einen Überblick über mein Dienstleistungsangebot geben.
In der beigefügten Word Datei finden Sie einen von mir erstellten Flyer-Text-Entwurf. Er soll lediglich als Orientierung dienen. Weitere Infos erhalten Sie auf meiner Homepage
www.praxis-tollring-quast.de.
Desweiteren erhalten Sie ein hochgeladenes Foto von mir, welches Sie bitte in Ihren Entwurf mit einbinden.
Ich bitte um Vorschläge für ein professionelles Design mit moderener gut lesbarer Schrift sowie farblich abgestimmten Blöcken des Inhalts.
Besonders wichtig ist mir die Orientierung an meinen Logofarben.
Das Logo wurde auch von gestaltwerk.de erstellt. Sie finden es unter meinen Projekten.
Für Rückfragen stehe ich Ihnen gerne zur Verfügung.
Freundliche Grüße
Sabine Tollring-Quast

```html
<!DOCTYPE html>
<html lang="de">
<head>
<meta charset="utf-8">
<title>Falzflyer Sabine Tollring-Quast</title>
<link href="https://fonts.googleapis.com/css2?family=Questrial&family=Roboto+Condensed:wght@400;700&display=swap" rel="stylesheet">
<style>
:root{
  --orange:#e8602a;
  --orange-light:#f28d2f;
  --paper:#ffffff;
  --paper-warm:#fdf3ec;
  --text:#5e5e5e;
  --stage:#40454e;
  --photo-wood:#a58a6a;
  --photo-green:#6f8f4a;
  --photo-asphalt:#5a5a5a;
  --photo-portrait:#bdbdbd;
}
*{box-sizing:border-box;margin:0;padding:0}
html,body{width:1200px;height:1039px;overflow:hidden}
body{background:var(--stage);font-family:"Questrial",sans-serif;color:var(--text);position:relative}
.spread{position:absolute;left:270px;width:660px;height:462px;display:flex;background:var(--paper);box-shadow:0 6px 18px rgba(0,0,0,.35)}
.spread--outside{top:38px}
.spread--inside{top:538px}
.panel{position:relative;width:220px;height:462px;overflow:hidden;border-right:1px solid #eee}
.panel:last-child{border-right:none}
.heading{font-family:"Roboto Condensed",sans-serif;font-weight:700;color:var(--orange);text-transform:uppercase;line-height:1.05}
.subheading{font-family:"Roboto Condensed",sans-serif;font-weight:400;color:var(--orange);text-transform:uppercase;font-size:10.5px;line-height:1.2}
.ticks{list-style:none;font-size:8.3px;line-height:1.35}
.ticks li{position:relative;padding-left:13px;margin-bottom:3px}
.ticks li::before{content:"";position:absolute;left:1px;top:2px;width:4px;height:7px;border:solid var(--orange);border-width:0 2px 2px 0;transform:rotate(40deg)}
.body-copy{font-size:8.3px;line-height:1.45}
.photo{position:absolute;display:block}

/* flap: quote */
.flap-band{position:absolute;left:0;top:0;width:220px;height:62px;background:linear-gradient(90deg,var(--orange),var(--orange-light))}
.quote{position:absolute;right:14px;top:12px;color:#fff;text-align:right;font-family:"Roboto Condensed",sans-serif;font-weight:700;font-size:11.5px;line-height:1.2}
.quote small{display:block;font-weight:400;font-size:8px;margin-top:2px}
.flap-photo{left:0;top:62px;width:220px;height:400px;background:linear-gradient(160deg,#6a6a6a,var(--photo-asphalt) 55%,#474747)}

/* back */
.back{background:linear-gradient(180deg,var(--paper-warm),var(--paper) 60%)}
.back .heading{font-size:20px;position:absolute;left:16px;top:26px}
.portrait{left:16px;top:62px;width:110px;height:78px;border-radius:0 0 28px 0;background:linear-gradient(140deg,#d7d7d7,var(--photo-portrait))}
.contact{position:absolute;left:16px;right:14px;top:152px;font-size:8.3px;line-height:1.45}
.contact .name{font-family:"Roboto Condensed",sans-serif;font-weight:700;color:var(--orange);font-size:10.5px}
.contact p{margin-bottom:9px}
.more{position:absolute;left:16px;right:14px;top:310px}
.more .subheading{margin-bottom:3px}
.url{position:absolute;left:16px;right:14px;top:372px;border-top:1px solid var(--orange);padding-top:6px;text-align:right;font-family:"Roboto Condensed",sans-serif;font-weight:700;color:var(--orange);font-size:9.5px}

/* cover */
.cover-band{position:absolute;left:0;top:0;width:220px;height:92px;background:linear-gradient(90deg,var(--orange),var(--orange-light))}
.brand{position:absolute;left:16px;top:24px;display:flex;align-items:center;gap:9px;color:#fff}
.brand-dot{width:24px;height:24px;border-radius:50%;border:2px solid #fff;flex:none}
.brand-name{font-size:15px;line-height:1.1}
.brand-tag{position:absolute;left:49px;right:10px;top:60px;color:#fff;font-size:7.6px;white-space:nowrap}
.cover-photo{left:0;top:92px;width:220px;height:250px;background:linear-gradient(170deg,var(--photo-green) 0%,#8f9d6a 22%,var(--photo-wood) 40%,#8c6f52 80%,#b9a48a 100%)}
.badge{position:absolute;left:112px;top:262px;width:98px;height:98px;border-radius:50%;background:linear-gradient(135deg,var(--orange-light),var(--orange));border:4px solid rgba(255,255,255,.85)}
.claim{position:absolute;left:16px;top:388px;color:var(--orange);font-size:16px;line-height:1.3}

/* inside */
.inside-band{position:absolute;left:0;top:0;height:36px;width:220px;background:linear-gradient(90deg,var(--orange),var(--orange-light))}
.intro-photo{left:0;top:36px;width:220px;height:96px;background:linear-gradient(160deg,#e9e4dc,#c9c2b4 60%,#7f93b0)}
.intro{position:absolute;left:16px;right:12px;top:146px}
.intro .heading{font-size:17px;margin-bottom:5px}
.intro .subheading{margin-bottom:8px}
.intro .body-copy{margin-top:12px}
.intro .body-copy p{margin-bottom:6px}

.services{position:absolute;left:16px;right:12px;top:18px}
.services .heading{font-size:17px;margin-bottom:3px}
.services .subheading{margin-bottom:6px}
.services section{margin-bottom:14px}
.panel--warm{background:linear-gradient(180deg,var(--paper-warm),var(--paper) 55%)}
.curves{position:absolute;left:0;top:0;pointer-events:none}
</style>
</head>
<body>

<div class="spread spread--outside">
  <article class="panel panel--flap">
    <div class="flap-band">
      <p class="quote">„Jeder Weg beginnt mit<br>dem ersten Schritt.“<small>(Sprichwort)</small></p>
    </div>
    <div class="photo flap-photo" role="img" aria-label="Foto: Füße auf Asphalt vor zwei gelben Richtungspfeilen"></div>
  </article>

  <article class="panel back">
    <h2 class="heading">Haben Sie Fragen?</h2>
    <div class="photo portrait" role="img" aria-label="Porträtfoto der Therapeutin in Schwarzweiß"></div>
    <div class="contact">
      <p><span class="name">SABINE TOLLRING-QUAST</span><br>Heilpraktikerin Psychotherapie (HeilprG)<br>Systemischer Coach (VBKL)</p>
      <p>Am Lindenhang 14<br>35091 Kirchwalden</p>
      <p>Telefon 06021 - 4837210<br>info@praxis-tollring-quast.de</p>
      <p>Rufen Sie mich an. Ich bin für Sie da!<br>Ich freue mich auf Ihren Besuch!</p>
    </div>
    <div class="more">
      <h3 class="subheading">Weitere Informationen</h3>
      <p class="body-copy">über mich und meine Angebote finden<br>Sie auf meiner Homepage.</p>
    </div>
    <p class="url">www.praxis-tollring-quast.de</p>
  </article>

  <article class="panel panel--cover">
    <div class="cover-band">
      <div class="brand"><span class="brand-dot"></span><span class="brand-name">Sabine Tollring-Quast</span></div>
      <p class="brand-tag">Psychotherapie | Coaching | Paarberatung</p>
    </div>
    <div class="photo cover-photo" role="img" aria-label="Foto: Holzstufen eines Waldweges zwischen grünen Pflanzen"></div>
    <svg class="curves" width="220" height="462" viewBox="0 0 220 462" aria-hidden="true">
      <path d="M0 104 Q110 80 220 98" fill="none" stroke="#f28d2f" stroke-width="1.5"/>
      <path d="M0 350 Q110 330 220 336" fill="none" stroke="#e8602a" stroke-width="1.5"/>
      <path d="M0 342 Q110 322 220 342 L220 462 L0 462Z" fill="#fff"/>
    </svg>
    <div class="badge" aria-hidden="true"></div>
    <p class="claim">Für mehr Zufriedenheit<br>im Privatleben und Beruf</p>
  </article>
</div>

<div class="spread spread--inside">
  <article class="panel">
    <div class="inside-band"></div>
    <div class="photo intro-photo" role="img" aria-label="Foto: Person am Schreibtisch mit Unterlagen"></div>
    <div class="intro">
      <h2 class="heading">Sie wünschen sich …</h2>
      <h3 class="subheading">Entlastung und<br>positive Veränderung?</h3>
      <ul class="ticks">
        <li>Sie sich in einer Lebens- oder Krisensituation befinden</li>
        <li>Sie Probleme allein nicht lösen können</li>
        <li>Sie mit Stress im Alltag kämpfen</li>
        <li>Sie sich antriebslos und ständig überfordert fühlen</li>
        <li>Sie unter Ängsten leiden, die Sie belasten</li>
      </ul>
      <div class="body-copy">
        <p>Jeder Mensch erlebt Phasen der Unzufriedenheit, die Unsicherheit und Sorgen auslösen.</p>
        <p>Wenn Veränderung nötig ist, können Psychotherapie, Coaching und Beratung hilfreich sein, um Lösungswege aus der Situation zu finden.</p>
      </div>
    </div>
  </article>

  <article class="panel panel--warm">
    <div class="services">
      <section>
        <h2 class="heading">Psychotherapie</h2>
        <h3 class="subheading">Behandlungsschwerpunkte:</h3>
        <ul class="ticks">
          <li>Ängste/Panikattacken</li>
          <li>Depression</li>
          <li>Stress/Burnout</li>
          <li>Lebenskrisen/schwere Belastungen</li>
          <li>Psychosomatische Beschwerden</li>
          <li>Paartherapie</li>
          <li>Stress- und Gesundheitstraining</li>
        </ul>
      </section>
      <section>
        <h2 class="heading">Coaching</h2>
        <h3 class="subheading">Begleitung in Veränderungsprozessen und schwierigen Lebenslagen/-krisen</h3>
        <ul class="ticks">
          <li>Veränderte Rahmenbedingungen im Privat- und Berufsleben wie z.B. Krankheit, Trennung, Trauer, Arbeitsplatzverlust u.a.</li>
          <li>Neuorientierung/Situationsbewertung</li>
          <li>Zielfindung</li>
          <li>Planung und Realisierung</li>
          <li>Lebensumbrüche wie z.B. Wechseljahre, Ruhestand u.a.</li>
        </ul>
      </section>
    </div>
  </article>

  <article class="panel panel--warm">
    <div class="services">
      <section>
        <h2 class="heading">Paarberatung</h2>
        <h3 class="subheading">Gemeinsam neue Wege finden</h3>
        <p class="body-copy">Wenn Streit und Distanz den Alltag prägen, unterstütze ich Sie dabei, Ihre Beziehung wieder bewusst und respektvoll so zu gestalten, wie Sie beide es sich wünschen.</p>
      </section>
      <section>
        <h2 class="heading">Persönlichkeits&shy;entwicklung</h2>
        <ul class="ticks">
          <li>Konflikte erkennen und konstruktiv lösen</li>
          <li>Beziehungs- und Lebensgestaltung</li>
          <li>Eigene Stärken entdecken, weiter entwickeln und nutzen</li>
          <li>Stressbewältigung/Burnoutprävention</li>
        </ul>
      </section>
    </div>
    <svg class="curves" width="220" height="462" viewBox="0 0 220 462" aria-hidden="true">
      <path d="M0 430 Q110 410 220 420" fill="none" stroke="#e8602a" stroke-width="1.5"/>
    </svg>
  </article>
</div>

</body>
</html>
```